Chiropractor needs a snazzy business card

Business card for a chiropractic office.
Office treats patients of all ages.
Focus is on a natural lifestyle.
Colors can include the logo colors as well as white and a little orange.
Ideally the card would have something chiropractic related such as a spine.

The back of the card should have a items for making appointments (date, times....)

```html
<!DOCTYPE html>
<html lang="en">
<head>
<meta charset="utf-8">
<title>Meadowlark Chiropractic – Business Card</title>
<link rel="stylesheet" href="https://fonts.googleapis.com/css2?family=Cinzel:wght@600;700&family=Crimson+Text:wght@400&display=swap">
<style>
  :root {
    --backdrop: #c9894a;
    --card: #e8e6d8;
    --navy: #124a78;
    --green: #4cae4c;
    --sage: #c4dcb6;
    --ink: #1c1c1c;
    --shadow: rgba(60, 30, 10, 0.35);
  }
  * { margin: 0; padding: 0; box-sizing: border-box; }
  html, body { width: 1200px; height: 1000px; overflow: hidden; }
  body { background: var(--backdrop); position: relative; }

  .card {
    position: absolute;
    width: 810px;
    background: var(--card);
    box-shadow: 2px 4px 10px var(--shadow);
  }
  .card--front { left: 210px; top: 30px; height: 490px; z-index: 2; }
  .card--back  { left: 165px; top: 480px; height: 450px; z-index: 1; }

  .holder-name {
    position: absolute; left: 70px; top: 62px;
    font-family: "Cinzel", serif; font-weight: 700;
    font-size: 42px; color: var(--navy); letter-spacing: 1px;
  }
  .phone {
    position: absolute; left: 66px; top: 118px;
    display: flex; align-items: center; gap: 18px;
    font-family: "Crimson Text", serif; font-size: 38px;
    color: var(--green); letter-spacing: 9px;
  }
  .phone svg { width: 30px; height: 38px; }

  .contact {
    position: absolute; font-family: "Crimson Text", serif;
    font-size: 17px; line-height: 20px; color: var(--ink);
    display: flex; gap: 12px; align-items: flex-start;
  }
  .contact svg { flex: none; }
  .contact--address { left: 56px; top: 305px; }
  .contact--web { left: 236px; top: 318px; align-items: center; }
  .contact--mail { left: 233px; top: 370px; align-items: center; }

  .accent-dot {
    position: absolute; right: 115px; top: 48px;
    width: 68px; height: 68px; border-radius: 50%;
    background: var(--sage);
  }

  .practice-name {
    position: absolute; left: 0; right: 0; top: 165px;
    text-align: center;
    font-family: "Cinzel", serif; font-weight: 600;
    color: var(--navy); font-size: 50px; line-height: 58px; letter-spacing: 3px;
  }
</style>
</head>
<body>
  <section class="card card--front">
    <div class="accent-dot"></div>
    <h1 class="holder-name">PUT YOUR NAME</h1>
    <div class="phone">
      <svg viewBox="0 0 24 30" aria-hidden="true"><path fill="#4cae4c" d="M5 1l4 0 2 7-3 2c1 4 3 8 6 10l3-2 5 4-2 5c-9 1-19-12-18-22z"/></svg>
      <span>555-014-2278</span>
    </div>
    <div class="contact contact--address">
      <svg width="24" height="32" viewBox="0 0 24 32" aria-hidden="true"><path fill="#4cae4c" d="M12 0a11 11 0 0 0-11 11c0 8 11 21 11 21s11-13 11-21A11 11 0 0 0 12 0z"/><circle cx="12" cy="11" r="4" fill="#e8e6d8"/></svg>
      <span>1065 Put Your<br>Address Here<br>City Here<br>4582</span>
    </div>
    <div class="contact contact--web">
      <svg width="26" height="26" viewBox="0 0 26 26" aria-hidden="true"><rect width="26" height="26" rx="4" fill="#4cae4c"/><g fill="none" stroke="#e8e6d8" stroke-width="1.3"><circle cx="13" cy="13" r="7"/><ellipse cx="13" cy="13" rx="3" ry="7"/><path d="M6 13h14M7 9.5h12M7 16.5h12"/></g></svg>
      <span>www.yourwebsite.com</span>
    </div>
    <div class="contact contact--mail">
      <svg width="28" height="20" viewBox="0 0 28 20" aria-hidden="true"><rect width="28" height="20" rx="2" fill="#4cae4c"/><path d="M1 2l13 10 13-10" fill="none" stroke="#e8e6d8" stroke-width="1.6"/></svg>
      <span>youremail@mailbox.com</span>
    </div>
  </section>

  <section class="card card--back">
    <h2 class="practice-name">MEADOWLARK<br>CHIROPRACTIC</h2>
  </section>
</body>
</html>
```